Mailer

Harbor Crest Partners, LLC
http://www.harborcrestpartnersllc.example/
412-863-2954
YOUR SUCCESS
You have an idea about where you want your business to go.  Need some help getting there? Are  you contemplating a transition to a new Broker Dealer, Producer Group or Custodian,  and/or interested in buying or selling a practice.
SOLUTIONS
Harbor Crest Partners, LLC is a consulting firm dedicated to  helping Finanial Advisors with their short term, and long term business affiliation and transition needs. W e interface with multple independent broker dealers and offer completely objective and unbiased guidance to help Financial Advisors find the perfect independent back office. Our services are free to you.

Industry/Entity Type
Business

```html
<!DOCTYPE html>
<html lang="en">
<head>
<meta charset="utf-8">
<title>Harbor Crest Partners Mailer</title>
<link href="https://fonts.googleapis.com/css2?family=Source+Sans+3:wght@400;600;700&display=swap" rel="stylesheet">
<style>
  :root {
    --brand-blue: #1a67ad;
    --sky-blue: #4a86cf;
    --sky-light: #8fb5e3;
    --snow: #f4f7fb;
    --ink: #1d1d1f;
    --rule: #8a8a8a;
    --page: #eceef1;
    --panel-fill: rgba(74, 128, 200, 0.55);
  }
  * { box-sizing: border-box; margin: 0; padding: 0; }
  html, body { width: 844px; height: 1200px; overflow: hidden; }
  body {
    background: var(--page);
    font-family: "Source Sans 3", "Myriad Pro", Arial, sans-serif;
    color: var(--ink);
    position: relative;
  }
  h1, h2, h3 { font-weight: 400; }

  /* ---------- Front of card ---------- */
  .card-front {
    position: absolute; left: 19px; top: 30px;
    width: 705px; height: 547px;
    overflow: hidden;
    box-shadow: 0 4px 14px rgba(0,0,0,0.25);
  }
  .front-photo {
    position: absolute; inset: 0;
    background:
      radial-gradient(ellipse 60% 70% at 62% 38%, #ffffff 0%, #e9eef5 45%, rgba(233,238,245,0) 75%),
      linear-gradient(115deg, var(--sky-blue) 0%, var(--sky-light) 40%, var(--snow) 70%, #dfe7f1 100%);
  }
  .front-company {
    position: absolute; top: 36px; right: 32px;
    color: #fff; font-size: 21px; font-weight: 400;
  }
  .front-headline {
    position: absolute; left: 51px; top: 254px;
    font-size: 25px; line-height: 30px; color: #1b2430;
  }
  .info-box {
    position: absolute; top: 364px;
    width: 304px; height: 146px;
    border: 1.5px solid rgba(255,255,255,0.9);
    border-radius: 14px;
    background: var(--panel-fill);
    color: #fff;
  }
  .info-box h2 { font-size: 21px; line-height: 24px; }
  .box-success { left: 37px; padding: 17px 12px 0 14px; }
  .box-success h2 { margin-bottom: 16px; }
  .box-success p { font-size: 13.4px; line-height: 16.8px; }
  .box-solutions { left: 365px; padding: 10px 6px 0 9px; }
  .box-solutions h2 { margin-bottom: 2px; }
  .box-solutions p { font-size: 12.2px; line-height: 15.1px; }

  /* ---------- Back of card ---------- */
  .card-back {
    position: absolute; left: 96px; top: 615px;
    width: 706px; height: 546px;
    background: #fff;
    overflow: hidden;
    box-shadow: 0 4px 14px rgba(0,0,0,0.25);
  }
  .back-photo {
    position: absolute; left: 0; right: 0; bottom: 0; height: 250px;
    background: linear-gradient(180deg, rgba(255,255,255,1) 0%, #e6e9ec 35%, #c9cdd1 65%, #8e9399 100%);
  }
  .message-panel {
    position: absolute; left: 0; top: 0;
    width: 394px; height: 408px;
    border-right: 1px solid #555;
    border-bottom: 1px solid #555;
    border-bottom-right-radius: 12px;
    background: linear-gradient(180deg, #fff 0%, #fff 72%, rgba(255,255,255,0) 100%);
  }
  .back-header {
    height: 81px; background: var(--brand-blue);
    color: #fff; text-align: center;
    font-size: 25px; line-height: 31px; padding-top: 9px;
  }
  .back-tagline {
    position: absolute; left: 30px; top: 113px;
    font-size: 16.5px; line-height: 20px;
  }
  .contact-heading {
    position: absolute; left: 28px; top: 193px;
    font-size: 18px; color: #333;
  }
  .contact-rule {
    position: absolute; left: 28px; top: 216px;
    width: 313px; height: 1px; background: #b8c2cc;
  }
  .contact-rule::before {
    content: ""; position: absolute; left: 0; top: -1px;
    width: 86px; height: 2px; background: var(--brand-blue);
  }
  .contact-list {
    position: absolute; left: 30px; top: 227px;
    list-style: none; font-size: 15px; line-height: 21px;
  }
  .contact-list .company { margin-bottom: 6px; }
  .contact-list strong { font-weight: 700; }
  .web-pill {
    position: absolute; left: 43px; top: 408px;
    width: 330px; height: 38px;
    background: var(--brand-blue);
    border-radius: 0 0 16px 16px;
    color: #fff; font-size: 18px; text-align: center; line-height: 37px;
    white-space: nowrap;
  }
  .stamp-box {
    position: absolute; left: 572px; top: 28px;
    width: 109px; height: 87px; border: 1px solid var(--rule);
  }
  .address-line {
    position: absolute; left: 413px; width: 266px; height: 1px; background: var(--rule);
  }
</style>
</head>
<body>

<section class="card-front">
  <div class="front-photo" role="img" aria-label="Photo of a skier jumping off a snow-covered cliff against a blue sky"></div>
  <p class="front-company">Harbor Crest Partners, LLC</p>
  <h1 class="front-headline">Some Dream Of Success.<br>We Make It Happen.</h1>
  <div class="info-box box-success">
    <h2>YOUR SUCCESS</h2>
    <p>You have an idea about where you want your business to go. Need some help getting there? Are you contemplating a transition to a new Broker Dealer, Producer Group or Custodian, and/or interested in buying or selling a practice.</p>
  </div>
  <div class="info-box box-solutions">
    <h2>SOLUTIONS</h2>
    <p>Harbor Crest Partners, LLC is a consulting firm dedicated to helping Finanial Advisors with their short term, and long term business affiliation and transition needs. We interface with multple independent broker dealers and offer completely objective and unbiased guidance to help Financial Advisors find the perfect independent back office. Our services are free to you.</p>
  </div>
</section>

<section class="card-back">
  <div class="back-photo" role="img" aria-label="Black and white photo of snowy mountain slopes with pine trees"></div>
  <div class="message-panel">
    <h2 class="back-header">Some Dream Of Success.<br>We Make It Happen.</h2>
    <p class="back-tagline">We’re an energetic, flexible, and hard working team<br>ready to make a difference for our clients.</p>
    <h3 class="contact-heading">Contact Us:</h3>
    <div class="contact-rule"></div>
    <ul class="contact-list">
      <li class="company">Harbor Crest Partners, LLC</li>
      <li>Phone: <strong>412-863-2954</strong></li>
      <li>Emil: <strong>Dana@harborcrestpartnersllc.example</strong></li>
      <li>Address: <strong>1487 Linden Ave, NW Washington, DC 20011</strong></li>
    </ul>
  </div>
  <div class="web-pill">www.harborcrestpartnersllc.example</div>
  <div class="stamp-box"></div>
  <div class="address-line" style="top:263px"></div>
  <div class="address-line" style="top:313px"></div>
  <div class="address-line" style="top:362px"></div>
</section>

</body>
</html>
```